Presentation Folder

We are looking for a design for a presentation folder given to clients upon first meeting.

Requirements
Must have
• Corporate contact information on one of the interior sleeves. Must use company logo. Full color interior and exterior. Should have similar feel to business cards and envelopes (see attached samples). If you have trouble with the template files for the folder size, you can visit this site (it is the last option on the page): http://zelvaro.net/g/showStaticPage.do?page=download_templates-pres.html

```html
<!DOCTYPE html>
<html lang="en">
<head>
<meta charset="utf-8">
<title>Birch Hollow Real Estate — Presentation Folder Interior</title>
<link rel="stylesheet" href="https://fonts.googleapis.com/css2?family=Cinzel:wght@400;600&display=swap">
<style>
  :root {
    --maroon: #7a2f35;
    --maroon-dark: #5e2228;
    --card: #86363d;
    --card-edge: rgba(255,255,255,0.45);
    --silver: #d9dadc;
    --silver-dark: #9ea2a6;
    --white: #ffffff;
    --sky: #9bb4d2;
    --brick: #8a5a48;
    --leaf: #6f9a45;
    --paper: #ecebe8;
  }
  * { box-sizing: border-box; margin: 0; padding: 0; }
  html, body { width: 1200px; height: 847px; overflow: hidden; background: var(--paper); }
  .folder-spread { position: relative; width: 1200px; height: 847px; }
  .hero-photo {
    position: absolute; inset: 0;
    background: linear-gradient(180deg, var(--sky) 0%, #b9c7d6 22%, #8f8a86 38%, var(--brick) 55%, #7d5a4b 70%, #5f7d3c 100%);
  }
  .hero-photo .foliage {
    position: absolute; right: 0; top: 0; width: 480px; height: 560px;
    background: radial-gradient(ellipse at 60% 55%, rgba(111,154,69,0.95) 0%, rgba(111,154,69,0.6) 45%, rgba(111,154,69,0) 75%);
  }
  .spine { position: absolute; left: 599px; top: 0; width: 2px; height: 847px; background: rgba(0,0,0,0.12); }
  .pockets { position: absolute; inset: 0; }
  .brand-mark {
    position: absolute; left: 120px; top: 640px; width: 360px; text-align: center;
    font-family: "Cinzel", serif; font-weight: 400; color: var(--white);
  }
  .brand-mark .brand-name { font-size: 40px; letter-spacing: 2px; line-height: 1.05; }
  .brand-mark .brand-sub { font-size: 20px; letter-spacing: 6px; }

  .business-card {
    position: absolute; left: 752px; top: 562px; width: 360px; height: 190px;
    filter: drop-shadow(0 2px 4px rgba(0,0,0,0.45));
    font-family: "Cinzel", serif; color: var(--white); font-weight: 400;
  }
  .card-face {
    position: absolute; inset: 0;
    background: var(--card-edge);
    clip-path: polygon(26px 0, 100% 0, 100% 100%, 0 100%, 0 26px);
  }
  .card-face::before {
    content: ""; position: absolute; inset: 1px;
    background: var(--card);
    clip-path: polygon(25px 0, 100% 0, 100% 100%, 0 100%, 0 25px);
  }
  .card-photo {
    position: absolute; right: 1px; top: 1px; width: 140px; height: 188px;
    background: linear-gradient(180deg, #8fb3dc 0%, #cfd9e2 50%, #e7e4de 100%);
    clip-path: polygon(36% 0, 100% 0, 100% 100%, 0 100%, 0 38%);
  }
  .card-brand { position: absolute; left: 20px; top: 34px; width: 170px; text-align: center; line-height: 1.15; }
  .card-brand .brand-name { font-size: 16px; }
  .card-brand .brand-sub { font-size: 8px; letter-spacing: 3px; }
  .card-contact { position: absolute; left: 16px; top: 92px; width: 200px; font-size: 8px; line-height: 1.5; }
  .card-contact .agent-name { font-size: 12px; letter-spacing: 1px; }
  .card-contact .agent-title { margin-bottom: 3px; }
  .card-badges { position: absolute; left: 176px; top: 164px; display: flex; gap: 4px; }
  .card-badges span { width: 12px; height: 12px; background: var(--white); }
</style>
</head>
<body>
<main class="folder-spread">
  <div class="hero-photo" role="img" aria-label="Photograph of a two-storey brick house with grey slate roof, white windows and a leafy green tree under a blue sky">
    <div class="foliage"></div>
  </div>
  <div class="spine"></div>

  <svg class="pockets" width="1200" height="847" viewBox="0 0 1200 847" aria-hidden="true">
    <defs>
      <linearGradient id="silverEdge" x1="0" x2="1" y1="0" y2="0">
        <stop offset="0" stop-color="#9ea2a6"/>
        <stop offset="0.5" stop-color="#ffffff"/>
        <stop offset="1" stop-color="#d9dadc"/>
      </linearGradient>
    </defs>
    <path class="pocket-edge" d="M0,500 L460,486 C540,484 578,600 596,847 L0,847 Z" fill="url(#silverEdge)"/>
    <path class="pocket" d="M0,510 L450,496 C518,494 552,600 570,847 L0,847 Z" fill="#7a2f35"/>
    <path class="pocket-edge" d="M604,847 C612,600 640,492 700,484 L1200,484 L1200,847 Z" fill="url(#silverEdge)"/>
    <path class="pocket" d="M628,847 C636,610 660,500 716,494 L1200,494 L1200,847 Z" fill="#7a2f35"/>
    <path class="card-slit" d="M742,590 L782,550" stroke="#5e2228" stroke-width="3"/>
    <path class="card-slit" d="M1102,764 L1124,742" stroke="#5e2228" stroke-width="3"/>
  </svg>

  <div class="brand-mark">
    <div class="brand-name">Birch Hollow</div>
    <div class="brand-sub">Real Estate</div>
  </div>

  <section class="business-card">
    <div class="card-face"></div>
    <div class="card-photo" role="img" aria-label="Portrait photo of the agent in shirt and tie against a suburban sky"></div>
    <div class="card-brand">
      <div class="brand-name">Birch Hollow</div>
      <div class="brand-sub">Real Estate</div>
    </div>
    <div class="card-contact">
      <div class="agent-name">Daniel Merrow</div>
      <div class="agent-title">Principal Broker &amp; Owner</div>
      <div>daniel@birchhollowhomes.com</div>
      <div>(410) 555-0148 Mobile</div>
      <div>(443) 555-0172 Office</div>
      <div>(443) 555-0193 Fax</div>
    </div>
    <div class="card-badges"><span></span><span></span></div>
  </section>
</main>
</body>
</html>
```